luxury contemporary fashion website needs simple, elegant flowchart to describe the buying and selli

* Luxury, resale, preloved items are sold on this online platform
*Horizontal, simple, flowchart with 5 steps in 'friendly' font with a simple emoticon/ picture for each step
*To be positioned in the 'How we work' tab of the webpage to explain in a very simple manner the buying and selling process for the customers.
*Attached is a very rudimentary mock-up of what we would like included and an idea of a project similar to what we desire
* to confirm the text for each step, we have also attached a word file below

Industry/Entity Type

Fashion

Font styles to use
Sans Serif

Colors
86cfc6
cfeae6

Requirements
Must have
• Simple drawing / shape after each point In the closest to 'duck egg blue' fill colour you can find with a black outline

```html
<!DOCTYPE html>
<html lang="en">
<head>
<meta charset="utf-8">
<title>Bespoke Concierge Service – How we work</title>
<link rel="stylesheet" href="https://fonts.googleapis.com/css2?family=Roboto:wght@300;400;700&family=Roboto+Slab:wght@500&display=swap">
<style>
  :root {
    --teal-band: #86cfc6;
    --duck-egg: #cfeae6;
    --teal-ink: #2a8089;
    --badge-outer: #55555a;
    --badge-inner: #3f3f44;
    --rule-grey: #c9c9c9;
    --white: #ffffff;
    --paper: #fdfdfd;
  }
  html, body {
    margin: 0;
    padding: 0;
    overflow: hidden;
    background: var(--paper);
  }
  .canvas {
    position: relative;
    width: 1200px;
    height: 848px;
    overflow: hidden;
    background: var(--paper);
    font-family: "Roboto", Arial, sans-serif;
  }
  .title-badge {
    position: absolute;
    left: 527px;
    top: 10px;
    width: 207px;
    height: 158px;
  }
  .title-rule {
    position: absolute;
    top: 82px;
    width: 148px;
    height: 5px;
    background: repeating-linear-gradient(90deg, var(--rule-grey) 0 4px, transparent 4px 6px);
  }
  .title-rule--left { left: 326px; }
  .title-rule--right { left: 786px; }

  .step-icon {
    position: absolute;
    top: 310px;
    width: 140px;
    height: 140px;
  }

  .steps-band {
    position: absolute;
    left: 0;
    top: 481px;
    width: 1200px;
    height: 367px;
    background: var(--teal-band);
  }
  .step {
    position: absolute;
    top: 26px;
    width: 240px;
    margin-left: -120px;
    text-align: center;
    color: var(--white);
  }
  .step-number {
    width: 38px;
    height: 38px;
    margin: 0 auto;
    border-radius: 50%;
    background: var(--white);
    color: var(--teal-ink);
    font-family: "Roboto Slab", Georgia, serif;
    font-weight: 500;
    font-size: 20px;
    line-height: 38px;
  }
  .step-title {
    margin: 22px 0 0;
    font-size: 20.5px;
    font-weight: 700;
    line-height: 24px;
  }
  .step-text {
    margin: 16px 0 0;
    font-size: 19px;
    font-weight: 300;
    line-height: 23px;
    white-space: pre-line;
  }
  .glyph {
    display: inline-block;
    vertical-align: -3px;
    width: 20px;
    height: 20px;
  }
</style>
</head>
<body>
<main class="canvas">

  <div class="title-rule title-rule--left"></div>
  <svg class="title-badge" viewBox="0 0 207 158" aria-label="Bespoke Concierge Service">
    <polygon points="0,22 103.5,0 207,22 207,136 103.5,158 0,136" fill="var(--badge-outer)"/>
    <polygon points="16,30 103.5,12 191,30 191,128 103.5,146 16,128" fill="var(--badge-inner)"/>
    <text x="103.5" y="52" text-anchor="middle" fill="#fff" font-family="Roboto, sans-serif" font-weight="300" font-size="22">BESPOKE</text>
    <text x="103.5" y="81" text-anchor="middle" fill="#fff" font-family="Roboto, sans-serif" font-weight="300" font-size="16.5">— CONCIERGE —</text>
    <text x="103.5" y="119" text-anchor="middle" fill="#fff" font-family="Roboto, sans-serif" font-weight="300" font-size="31">SERVICE</text>
  </svg>
  <div class="title-rule title-rule--right"></div>

  <!-- Step icons -->
  <svg class="step-icon" style="left:96px" viewBox="-70 -70 140 140" aria-hidden="true">
    <polygon fill="var(--duck-egg)" stroke="var(--teal-ink)" stroke-width="6" stroke-linejoin="round"
      points="58,0 46.1,9.2 53.6,22.2 39.1,26.1 41,41 26.1,39.1 22.2,53.6 9.2,46.1 0,58 -9.2,46.1 -22.2,53.6 -26.1,39.1 -41,41 -39.1,26.1 -53.6,22.2 -46.1,9.2 -58,0 -46.1,-9.2 -53.6,-22.2 -39.1,-26.1 -41,-41 -26.1,-39.1 -22.2,-53.6 -9.2,-46.1 0,-58 9.2,-46.1 22.2,-53.6 26.1,-39.1 41,-41 39.1,-26.1 53.6,-22.2 46.1,-9.2"/>
    <polygon fill="none" stroke="#fff" stroke-width="3" stroke-linejoin="round" transform="scale(0.8)"
      points="58,0 46.1,9.2 53.6,22.2 39.1,26.1 41,41 26.1,39.1 22.2,53.6 9.2,46.1 0,58 -9.2,46.1 -22.2,53.6 -26.1,39.1 -41,41 -39.1,26.1 -53.6,22.2 -46.1,9.2 -58,0 -46.1,-9.2 -53.6,-22.2 -39.1,-26.1 -41,-41 -26.1,-39.1 -22.2,-53.6 -9.2,-46.1 0,-58 9.2,-46.1 22.2,-53.6 26.1,-39.1 41,-41 39.1,-26.1 53.6,-22.2 46.1,-9.2"/>
    <text x="0" y="8" text-anchor="middle" fill="#fff" stroke="var(--teal-ink)" stroke-width="1" font-family="Georgia, serif" font-weight="700" font-size="21">NEW</text>
  </svg>

  <svg class="step-icon" style="left:331px" viewBox="0 0 140 140" aria-hidden="true">
    <path d="M70 42 C55 20 38 22 42 34 C45 42 60 44 70 42 Z" fill="var(--duck-egg)"/>
    <path d="M70 42 C85 20 102 22 98 34 C95 42 80 44 70 42 Z" fill="var(--duck-egg)"/>
    <polygon points="14,28 24,46 14,46" fill="var(--duck-egg)"/>
    <polygon points="126,28 116,46 126,46" fill="var(--duck-egg)"/>
    <rect x="14" y="46" width="112" height="26" fill="var(--teal-ink)"/>
    <rect x="18" y="76" width="104" height="46" fill="var(--teal-ink)"/>
    <rect x="57" y="42" width="26" height="80" fill="var(--duck-egg)"/>
  </svg>

  <svg class="step-icon" style="left:556px" viewBox="0 0 140 140" aria-hidden="true">
    <rect x="50" y="22" width="44" height="40" fill="var(--duck-egg)" transform="rotate(-10 72 42)"/>
    <path d="M4 34 H24 L40 100 H106" fill="none" stroke="var(--teal-ink)" stroke-width="5" stroke-linejoin="round"/>
    <path d="M28 50 H116 L104 90 H37" fill="none" stroke="var(--teal-ink)" stroke-width="5" stroke-linejoin="round"/>
    <path d="M31 63 H112 M34 77 H108 M52 50 L54 90 M74 50 L73 90 M96 50 L91 90" stroke="var(--teal-ink)" stroke-width="4"/>
    <circle cx="57" cy="114" r="8" fill="#fff" stroke="var(--teal-ink)" stroke-width="5"/>
    <circle cx="90" cy="114" r="8" fill="#fff" stroke="var(--teal-ink)" stroke-width="5"/>
  </svg>

  <svg class="step-icon" style="left:764px" viewBox="0 0 140 140" aria-hidden="true">
    <rect x="28" y="26" width="70" height="96" rx="2" fill="#fff" stroke="var(--teal-ink)" stroke-width="4"/>
    <rect x="51" y="16" width="24" height="16" fill="var(--teal-ink)"/>
    <g fill="none" stroke="var(--duck-egg)" stroke-width="4" stroke-linecap="round">
      <path d="M38 50 l5 5 l9 -9"/><path d="M38 72 l5 5 l9 -9"/><path d="M38 94 l5 5 l9 -9"/>
    </g>
    <g stroke="var(--teal-ink)" stroke-width="4">
      <path d="M62 46 H88 M62 56 H88 M62 68 H88 M62 78 H88 M62 90 H88 M62 100 H88"/>
    </g>
    <rect x="106" y="62" width="12" height="60" fill="#fff" stroke="var(--teal-ink)" stroke-width="3"/>
    <line x1="112" y1="62" x2="112" y2="122" stroke="var(--teal-ink)" stroke-width="2"/>
    <polygon points="106,62 118,62 112,52" fill="var(--teal-ink)"/>
  </svg>

  <svg class="step-icon" style="left:976px" viewBox="0 0 140 140" aria-hidden="true">
    <rect x="40" y="20" width="80" height="42" fill="var(--duck-egg)" transform="rotate(14 80 41)"/>
    <text x="55" y="47" fill="var(--teal-ink)" font-family="Georgia, serif" font-size="20" font-weight="700">$</text>
    <rect x="16" y="54" width="102" height="68" rx="5" fill="#fff" stroke="var(--teal-ink)" stroke-width="5"/>
    <rect x="74" y="76" width="48" height="26" rx="4" fill="var(--teal-ink)"/>
    <circle cx="89" cy="89" r="5" fill="var(--duck-egg)"/>
  </svg>

  <!-- Steps -->
  <section class="steps-band" aria-label="How we work">
    <div class="step" style="left:166px">
      <div class="step-number">1</div>
      <h2 class="step-title">Have items to sell?</h2>
      <p class="step-text">- brand spanking
        or nearly new <svg class="glyph" viewBox="0 0 20 20" aria-hidden="true"><path fill="var(--teal-ink)" d="M6 3 l1.3 3 3 .3 -2.3 2 .7 3 -2.7-1.6 -2.7 1.6 .7-3 -2.3-2 3-.3z M14 9 l1.2 2.6 2.8 .3 -2.1 1.9 .6 2.8 -2.5-1.5 -2.5 1.5 .6-2.8 -2.1-1.9 2.8-.3z"/></svg></p>
    </div>
    <div class="step" style="left:401px">
      <div class="step-number">2</div>
      <h2 class="step-title">Personal collection</h2>
      <p class="step-text">- we choose the
        pieces we know
        thelumeo custom-
        ers will love <svg class="glyph" viewBox="0 0 20 20" aria-hidden="true"><path fill="var(--teal-ink)" d="M10 17 L3 10 A4 4 0 0 1 10 5 A4 4 0 0 1 17 10 Z"/></svg></p>
    </div>
    <div class="step" style="left:629px">
      <div class="step-number">3</div>
      <h2 class="step-title">We parpare</h2>
      <p class="step-text">- your item for sale
        with thorough authe
        ticity &amp; condition
        checks... so you
        don’t have to <svg class="glyph" viewBox="0 0 20 20" aria-hidden="true"><circle cx="10" cy="10" r="8" fill="none" stroke="var(--teal-ink)" stroke-width="1.8"/><circle cx="7.3" cy="8" r="1.2" fill="var(--teal-ink)"/><circle cx="12.7" cy="8" r="1.2" fill="var(--teal-ink)"/><path d="M6 11.5 Q10 15.5 14 11.5" fill="none" stroke="var(--teal-ink)" stroke-width="1.6"/></svg></p>
    </div>
    <div class="step" style="left:834px">
      <div class="step-number">4</div>
      <h2 class="step-title">Once sold</h2>
      <p class="step-text">- we loving prepare
        the itm
        - shipped via tracked
        services <svg class="glyph" viewBox="0 0 20 20" aria-hidden="true"><path fill="var(--teal-ink)" d="M9 2 h2 v6 l7 4 v2 l-7-2 v4 l2 2 v1 l-3-1 -3 1 v-1 l2-2 v-4 l-7 2 v-2 l7-4z"/></svg></p>
    </div>
    <div class="step" style="left:1046px">
      <div class="step-number">5</div>
      <h2 class="step-title">Your payment</h2>
      <p class="step-text">i) pocket the cash
        ii) donate to charity
        - full or partial
        amount <span style="color:var(--teal-ink);font-weight:700">$</span></p>
    </div>
  </section>

</main>
</body>
</html>
```